Smart, Classy, Conservative looking Legal Letterhead

I need a letterhead that when you look at it it "says to you " this is a well established law firm with very smart lawyers, which will one day be appearing before the Supreme Court of the USA. All information about the Law firm should appear at the top of the page. please no information in the footer.

Industry/Entity Type

Legal

Requirements
Must have
• The name of the law firm, both addresses, phone number and fax,, The names of the attorneys, the website.
• Fields that get changed such as the date, VIA, Address of who the letter is going to,
• Re, Index,
• should have a clean neat look, sleek
Nice to have
• some color would be nice. A logo of some sort could be nice as well. Maybe a single S or interlocking P's For Pelworth and Pelworth.
Should not have
• not too modern looking.

```html
<!DOCTYPE html>
<html lang="en">
<head>
<meta charset="utf-8">
<title>Pelworth &amp; Pelworth Letterhead</title>
<link rel="stylesheet" href="https://fonts.googleapis.com/css2?family=Tinos:ital,wght@0,400;0,700;1,400&display=swap">
<style>
  :root {
    --backdrop: #d6d6d6;
    --paper: #ffffff;
    --ink: #111111;
    --gold: #b8962a;
    --band-copper: #a8662a;
    --band-gold: #d8b92c;
    --band-olive: #9c8a2c;
    --band-text: #ffffff;
  }
  * { margin: 0; padding: 0; box-sizing: border-box; }
  html, body {
    width: 1200px; height: 900px; overflow: hidden;
    background: var(--backdrop);
    font-family: "Tinos", "Times New Roman", serif;
    color: var(--ink);
  }
  .letterhead {
    position: absolute; left: 300px; top: 28px;
    width: 600px; height: 842px;
    background: var(--paper);
  }
  .letterhead > * { position: absolute; }
  .brand-mark {
    left: 20px; top: 40px; width: 64px;
    font-size: 15px; font-weight: 700; line-height: 1.15;
    color: var(--gold); text-align: center;
  }
  .firm-header {
    left: 0; width: 600px; top: 26px; text-align: center;
  }
  .firm-name { font-size: 21px; font-weight: 700; letter-spacing: 0.3px; line-height: 24px; }
  .firm-tagline { font-size: 16.5px; font-weight: 700; line-height: 20px; }
  .firm-addresses { font-size: 10px; line-height: 12px; margin-top: 2px; }
  .firm-addresses span { display: inline-block; margin: 0 4px; }
  .firm-web { font-size: 10px; margin-top: 4px; }
  .letter-date { font-size: 17px; font-style: italic; margin-top: 4px; }
  .recipient, .attorney-list {
    top: 146px; font-size: 10px; line-height: 12.2px;
  }
  .recipient { left: 22px; }
  .attorney-list { right: 22px; text-align: right; font-weight: 700; }
  .delivery-method { font-weight: 700; }
  .reference {
    top: 238px; left: 0; width: 600px; text-align: center;
    font-size: 10px; line-height: 12px;
  }
  .reference b { font-weight: 700; }
  .letter-body {
    left: 22px; top: 279px; width: 558px;
    font-size: 10px; line-height: 12.4px;
  }
  .letter-body p { margin-bottom: 12.4px; }
  .letter-body .indent { text-indent: 58px; }
  .cc-line { left: 22px; top: 738px; font-size: 10px; }
  .cc-line b { font-weight: 700; }
  .footer-band {
    left: 0; bottom: 0; width: 600px; height: 80px;
    background: linear-gradient(100deg, var(--band-copper) 0%, var(--band-gold) 48%, var(--band-olive) 100%);
  }
  .footer-mark {
    position: absolute; right: 14px; top: 24px;
    font-size: 13px; font-weight: 700; color: var(--band-text);
  }
</style>
</head>
<body>
  <main class="letterhead">
    <div class="brand-mark">Pelworth<br>&amp;<br>Pelworth</div>

    <header class="firm-header">
      <div class="firm-name">PELWORTH &amp; PELWORTH</div>
      <div class="firm-tagline">ATTORNEYS AT LAW</div>
      <div class="firm-addresses">
        <span>414 MADE UP STREET<br>TOWN, STATE 39440</span>
        <span>414 MADE UP STREET<br>TOWN, STATE 39440</span>
      </div>
      <div class="firm-web">WWW.WEBSITE.COM</div>
      <div class="letter-date">July 1st 2015</div>
    </header>

    <address class="recipient" style="font-style:normal">
      <div class="delivery-method">VIA COURIER</div>
      Hon. Fake Judge Name Here<br>
      United States District Court, E.D.N.Y<br>
      200 Civic Plaza<br>
      Courtroom 99999<br>
      Harbor Point, NY 11790-0000
    </address>

    <ul class="attorney-list" style="list-style:none">
      <li>Daniel A. Pelworth</li>
      <li>Martin J. Haldane</li>
      <li>Jonathan R. Whitcombe</li>
      <li>Helena M. Corbett</li>
      <li>Edward T. Linwood</li>
      <li>Marian E. Holloway</li>
    </ul>

    <div class="reference">
      <div><b>Re:</b> XXXXXXXXXXXXXXXXXXXXXXXXXXXXXXXX</div>
      <div><b>Index:</b> XXXXXXXXXXXXXXXXXXXXXXXXXXXXXXXX</div>
    </div>

    <section class="letter-body">
      <p>Your Honour,</p>
      <p class="indent">Pursuant to Your Honor’s Individual Practises Rule III(C)(3), enclosed please find a courtesy copy of Plaintiffs Revised. Lorem ipsum dolor sit amet, consectetur adipiscing elit, sed do eiusmod tempor incididunt ut labore et dolore magna aliqua. Ut enim ad minim veniam, quis nostrud exercitation ullamco laboris nisi ut aliquip ex ea commodo consequat.</p>
      <p>Duis aute irure dolo in reprehenderit in voluptate velit esse cillum dolore eu fugiat nulla pariatur. Excepteur sint occaecat cupidatat non proident, sunt in culpa qui officia deserunt mollit anim id est laborum.</p>
      <p>Respectfully,<br>Daniel A. Pelworth</p>
    </section>

    <div class="cc-line"><b>CC:</b> Fake opposing counsel name here</div>

    <footer class="footer-band">
      <div class="footer-mark">Pelworth</div>
    </footer>
  </main>
</body>
</html>
```